Property Management Company looking for a high-end business card, letterhead and envelope design.

We provide high-end / boutique property management for real estate investors or individuals looking for someone to manage their portfolio. we are looking for a cohesive high-end design for our business cards, letterhead and envelopes.

Target Market(s)

Real Estate Investors

Industry/Entity Type

Real Estate

Requirements
Must have
• business card, letterhead and envelope design - logo attached

```html
<!DOCTYPE html>
<html lang="en">
<head>
<meta charset="utf-8">
<title>Keystead Property Management — Stationery</title>
<link rel="stylesheet" href="https://fonts.googleapis.com/css2?family=Lato:ital,wght@0,300;0,400;0,700;1,400&display=swap">
<style>
  :root{
    --navy:#004370;
    --navy-soft:#3f78a0;
    --band:#9e9e9e;
    --band-light:#bdbdbd;
    --paper:#ffffff;
    --ink:#4a4a4a;
    --muted:#8a8a8a;
    --stage-1:#c4c4c4;
    --stage-2:#f0f0f0;
    --stage-3:#dedede;
  }
  *{box-sizing:border-box;margin:0;padding:0}
  html,body{width:1200px;height:2472px;overflow:hidden}
  body{font-family:"Lato",Arial,sans-serif;color:var(--ink);position:relative}
  .stage{position:absolute;left:0;width:1200px}
  .stage--cards{top:0;height:790px;background:linear-gradient(160deg,#a9a9a9 0%,var(--stage-1) 55%,#d6d6d6 100%)}
  .stage--letter{top:790px;height:840px;background:var(--stage-2)}
  .stage--envelope{top:1630px;height:842px;background:var(--stage-3)}

  .sheet{position:absolute;background:var(--paper);overflow:hidden;box-shadow:0 10px 30px rgba(0,0,0,.18)}
  .sheet svg.decor{position:absolute;inset:0;width:100%;height:100%}

  .brand{font-family:"Lato",Arial,sans-serif;font-weight:700;color:var(--navy);text-transform:uppercase;line-height:1.05}
  .brand span{display:block}

  /* business cards */
  .card{width:430px;height:250px;top:270px}
  .card--front{left:110px;background:var(--navy)}
  .card--front .brand{position:absolute;left:0;right:0;top:88px;text-align:center;color:#fff;font-size:34px;letter-spacing:6px}
  .card--front .brand span+span{font-size:13px;letter-spacing:5px;margin-top:8px}
  .card--back{left:660px}
  .card--back .brand{position:absolute;left:34px;top:70px;font-size:22px;letter-spacing:3px}
  .card--back .brand span+span{font-size:9px;letter-spacing:2.5px;margin-top:3px}
  .card__name{position:absolute;left:34px;top:128px;font-size:16px;color:var(--muted)}
  .card__role{position:absolute;left:34px;top:148px;font-size:9px;font-weight:700;color:var(--navy);letter-spacing:.5px}
  .card__contacts{position:absolute;left:34px;top:176px;font-size:9px;line-height:15px;color:var(--ink);list-style:none}
  .card__contacts li{display:flex;align-items:center;gap:6px}
  .card__contacts--right{left:222px;top:176px}

  .icon{width:9px;height:9px;flex:none;fill:var(--navy)}

  /* letterhead */
  .letterhead{width:520px;height:736px;left:340px;top:52px}
  .letterhead .brand{position:absolute;left:190px;top:46px;font-size:22px;letter-spacing:3px}
  .letterhead .brand span+span{font-size:8.5px;letter-spacing:2.5px;margin-top:3px}
  .recipient{position:absolute;left:52px;top:112px;font-size:8px;line-height:11px;color:var(--muted)}
  .recipient__to{font-size:7px}
  .recipient__name{font-size:15px;font-weight:700;color:var(--navy);line-height:18px}
  .recipient b{color:var(--navy)}
  .letter__date{position:absolute;right:48px;top:112px;font-size:7.5px;color:var(--muted);font-style:italic}
  .letter__greeting{position:absolute;left:52px;top:196px;font-size:8px;color:var(--muted)}
  .letter__body{position:absolute;left:52px;right:52px;top:220px;font-size:8px;line-height:12.5px;color:var(--muted)}
  .letter__body p{margin-bottom:10px}
  .letter__body p.lead{color:var(--ink);font-weight:700}
  .signoff{position:absolute;left:52px;top:390px}
  .signoff__name{font-size:12px;font-weight:700;color:#222}
  .signoff__role{font-size:7px;color:var(--muted)}
  .signoff__mark{width:110px;height:30px;margin-top:6px;border-radius:3px;background:linear-gradient(90deg,rgba(63,120,160,.25),rgba(63,120,160,.08))}
  .letter__contacts{position:absolute;left:52px;top:476px;font-size:7.5px;line-height:13px;color:var(--muted);list-style:none}
  .letter__contacts li{display:flex;align-items:center;gap:6px}
  .letter__contacts .icon{width:7px;height:7px}

  /* envelope */
  .envelope{width:960px;height:470px;left:120px;top:186px}
  .envelope .brand{position:absolute;left:70px;top:110px;font-size:40px;letter-spacing:6px}
  .envelope .brand span+span{font-size:15px;letter-spacing:4.5px;margin-top:5px}
  .envelope__window{position:absolute;left:610px;top:200px;width:250px;height:120px;border-radius:10px;background:linear-gradient(120deg,#1f5d8c 0%,#3a79a6 55%,#1f5d8c 100%);box-shadow:0 4px 10px rgba(0,0,0,.15)}
  .envelope__contacts{position:absolute;left:120px;top:300px;font-size:19px;line-height:30px;color:var(--ink);list-style:none;font-weight:300}
  .envelope__contacts li{display:flex;align-items:center;gap:14px}
  .envelope__contacts .icon{width:16px;height:16px}
</style>
</head>
<body>

<svg width="0" height="0" style="position:absolute" aria-hidden="true">
  <defs>
    <linearGradient id="fade-strip" x1="0" x2="1" y1="0" y2="0">
      <stop offset="0" stop-color="#004370"/>
      <stop offset="1" stop-color="#004370" stop-opacity="0"/>
    </linearGradient>
    <symbol id="i-pin" viewBox="0 0 10 10"><path d="M5 0a3.6 3.6 0 0 0-3.6 3.6C1.4 6.4 5 10 5 10s3.6-3.6 3.6-6.4A3.6 3.6 0 0 0 5 0zm0 5a1.4 1.4 0 1 1 0-2.8A1.4 1.4 0 0 1 5 5z"/></symbol>
    <symbol id="i-phone" viewBox="0 0 10 10"><path d="M2.2 0.5 3.8 2.6 2.9 3.7c.6 1.4 1.9 2.7 3.4 3.4l1.1-.9 2.1 1.6-1 1.7C4.6 9.3.7 5.4.5 1.5z"/></symbol>
    <symbol id="i-send" viewBox="0 0 10 10"><path d="M10 0 0 4.2l3.6 1.4L4.8 10z"/></symbol>
    <symbol id="i-link" viewBox="0 0 10 10"><path d="M4.2 5.8a2 2 0 0 1 0-2.8l1.6-1.6a2 2 0 0 1 2.8 2.8l-.8.8-.8-.8.8-.8a.9.9 0 0 0-1.2-1.2L5 3.8a.9.9 0 0 0 0 1.2zM5.8 4.2a2 2 0 0 1 0 2.8L4.2 8.6a2 2 0 0 1-2.8-2.8l.8-.8.8.8-.8.8a.9.9 0 0 0 1.2 1.2L5 6.2a.9.9 0 0 0 0-1.2z"/></symbol>
  </defs>
</svg>

<!-- Business cards -->
<section class="stage stage--cards">
  <article class="sheet card card--front">
    <div class="brand"><span>Keystead</span><span>Property Management</span></div>
  </article>

  <article class="sheet card card--back">
    <svg class="decor" viewBox="0 0 430 250" preserveAspectRatio="none" aria-hidden="true">
      <polygon points="215,0 430,0 430,190" fill="var(--band)"/>
      <polygon points="330,0 430,0 430,86" fill="#fff"/>
      <polygon points="352,0 430,0 430,66" fill="var(--navy)"/>
      <polygon points="0,178 0,250 96,250" fill="var(--band)"/>
      <polygon points="170,42 232,42 238,50 176,50" fill="url(#fade-strip)"/>
      <polygon points="336,184 420,184 426,192 342,192" fill="url(#fade-strip)" transform="rotate(180 381 188)"/>
    </svg>
    <div class="brand"><span>Keystead</span><span>Property Management</span></div>
    <div class="card__name">Your full name</div>
    <div class="card__role">Designation</div>
    <ul class="card__contacts">
      <li><svg class="icon"><use href="#i-phone"/></svg>(+00) 555 0192 340</li>
      <li><svg class="icon"><use href="#i-pin"/></svg>27 Birchfield Lane, Larkton, CT 06000</li>
      <li><svg class="icon"><use href="#i-link"/></svg>www.keysteadproperty.com</li>
    </ul>
    <ul class="card__contacts card__contacts--right">
      <li><svg class="icon"><use href="#i-send"/></svg>hello@keysteadproperty.com</li>
    </ul>
  </article>
</section>

<!-- Letterhead -->
<section class="stage stage--letter">
  <article class="sheet letterhead">
    <svg class="decor" viewBox="0 0 520 736" preserveAspectRatio="none" aria-hidden="true">
      <polygon points="400,0 520,0 520,150" fill="var(--band)"/>
      <polygon points="462,0 520,0 520,72" fill="#fff"/>
      <polygon points="476,0 520,0 520,55" fill="var(--navy)"/>
      <polygon points="380,0 392,0 392,30 380,30" fill="url(#fade-strip)" transform="rotate(90 386 15)"/>
      <polygon points="0,650 0,736 40,736" fill="var(--navy)"/>
      <polygon points="60,736 74,736 74,700 60,700" fill="var(--navy)" opacity=".85"/>
    </svg>
    <div class="brand"><span>Keystead</span><span>Property Management</span></div>
    <div class="recipient">
      <div class="recipient__to">To</div>
      <div class="recipient__name">Marcus</div>
      <div>Director</div>
      <div><b>Address</b> : 18 Maple Row, Brookfield, IL 60500</div>
      <div><b>Email</b> : marcus@mailbox.com</div>
      <div><b>Phone</b> : (+00) 555 0178 210</div>
    </div>
    <div class="letter__date">Date : 27.07.2019</div>
    <div class="letter__greeting">Dear Mr.,_________</div>
    <div class="letter__body">
      <p>We are pleased to confirm that your portfolio review is complete. Our team has prepared a full report on each property, covering tenancy, upkeep and yearly returns, along with clear steps we suggest for the months ahead.</p>
      <p class="lead">Please review the enclosed summary and let us know a time that suits you to talk it through.</p>
      <p>Thank you for trusting us with your investments. We look forward to a long and rewarding partnership.</p>
    </div>
    <div class="signoff">
      <div class="signoff__name">Your Name</div>
      <div class="signoff__role">Designation</div>
      <div class="signoff__mark" role="img" aria-label="Space for handwritten signature"></div>
    </div>
    <ul class="letter__contacts">
      <li><svg class="icon"><use href="#i-pin"/></svg>27 Birchfield Lane, Larkton, CT 06000</li>
      <li><svg class="icon"><use href="#i-phone"/></svg>(+00) 555 0192 340</li>
      <li><svg class="icon"><use href="#i-send"/></svg>hello@keysteadproperty.com</li>
      <li><svg class="icon"><use href="#i-link"/></svg>www.keysteadproperty.com</li>
    </ul>
  </article>
</section>

<!-- Envelope -->
<section class="stage stage--envelope">
  <article class="sheet envelope">
    <svg class="decor" viewBox="0 0 960 470" preserveAspectRatio="none" aria-hidden="true">
      <polygon points="460,0 960,0 960,330" fill="var(--band)"/>
      <polygon points="660,0 960,0 960,190" fill="#fff"/>
      <polygon points="700,0 960,0 960,150" fill="var(--navy)"/>
      <polygon points="0,350 0,470 170,470" fill="var(--band)"/>
      <polygon points="380,40 520,40 532,56 392,56" fill="url(#fade-strip)"/>
      <polygon points="860,300 950,300 960,314 870,314" fill="url(#fade-strip)" transform="rotate(180 910 307)"/>
    </svg>
    <div class="brand"><span>Keystead</span><span>Property Management</span></div>
    <div class="envelope__window"></div>
    <ul class="envelope__contacts">
      <li><svg class="icon"><use href="#i-pin"/></svg>27 Birchfield Lane, Larkton, CT 06000</li>
      <li><svg class="icon"><use href="#i-phone"/></svg>(+00) 555 0192 340</li>
      <li><svg class="icon"><use href="#i-send"/></svg>hello@keysteadproperty.com</li>
      <li><svg class="icon"><use href="#i-link"/></svg>www.keysteadproperty.com</li>
    </ul>
  </article>
</section>

</body>
</html>
```